International wholesale business needs a business card

We need a business card.

Company Details:
Company Name and logo
Address, Phone number, Website
Employee Details:
Name, Designation, Mobile Number & Email address

```html
<!DOCTYPE html>
<html lang="en">
<head>
<meta charset="utf-8">
<title>Kestrel Trading – Business Card</title>
<link rel="stylesheet" href="https://fonts.googleapis.com/css2?family=Montserrat:wght@400;500;700&display=swap">
<style>
  :root {
    --page: #2a2a2d;
    --card: #1f1f21;
    --red: #c8262c;
    --grey: #a7aaad;
    --white: #f2f2f2;
  }
  * { margin: 0; padding: 0; box-sizing: border-box; }
  html, body { width: 1200px; height: 900px; overflow: hidden; }
  body {
    background: var(--page);
    font-family: "Montserrat", sans-serif;
    display: flex;
    flex-direction: column;
    align-items: center;
    justify-content: center;
    gap: 44px;
  }
  .card {
    position: relative;
    width: 700px;
    height: 400px;
    background: var(--card);
    border-radius: 16px;
    overflow: hidden;
  }
  .brand {
    display: flex;
    align-items: center;
    gap: 22px;
    color: var(--red);
    font-weight: 700;
    letter-spacing: 3px;
    text-transform: uppercase;
  }
  .brand-dot {
    width: 74px; height: 74px;
    border-radius: 50%;
    background: var(--red);
    flex: none;
  }
  .brand-name { font-size: 52px; line-height: 1; }

  /* Front */
  .card-front .brand {
    position: absolute;
    left: 0; right: 0; top: 50%;
    transform: translateY(-50%);
    justify-content: center;
  }
  .card-front .edge-band {
    position: absolute; left: 0; right: 0; bottom: 0;
    height: 8px; background: var(--red);
  }

  /* Back */
  .card-back .brand {
    position: absolute; left: 60px; top: 70px;
  }
  .card-back .brand-dot { width: 60px; height: 60px; }
  .card-back .brand-name { font-size: 42px; }
  .details {
    position: absolute; left: 60px; right: 50px; top: 205px;
    display: flex; align-items: stretch; gap: 26px;
  }
  .person { text-align: right; color: var(--white); font-size: 15px; line-height: 1.5; }
  .person-name { color: var(--red); font-weight: 700; font-size: 24px; line-height: 1.2; }
  .divider { width: 1.5px; background: var(--red); }
  .contact { list-style: none; color: var(--white); font-size: 15px; line-height: 1.9; }
  .contact li { display: flex; align-items: center; gap: 10px; }
  .contact svg { width: 14px; height: 14px; fill: var(--red); flex: none; }
  .bottom-band {
    position: absolute; left: 0; right: 0; bottom: 0; height: 14px;
    display: flex;
  }
  .bottom-band .band-red { flex: 4; background: var(--red); }
  .bottom-band .band-grey { flex: 1; background: var(--grey); }
</style>
</head>
<body>
  <section class="card card-front">
    <div class="brand">
      <span class="brand-dot"></span>
      <span class="brand-name">Kestrel Trading</span>
    </div>
    <div class="edge-band"></div>
  </section>

  <section class="card card-back">
    <div class="brand">
      <span class="brand-dot"></span>
      <span class="brand-name">Kestrel Trading</span>
    </div>
    <div class="details">
      <div class="person">
        <p class="person-name">Daniel Moreau</p>
        <p class="person-role">CEO &amp; Founder</p>
        <p class="person-address">Parque Norte C/3 nº 8<br>2207 Villanueva del Río</p>
      </div>
      <div class="divider"></div>
      <ul class="contact">
        <li>
          <svg viewBox="0 0 16 16" aria-hidden="true"><path d="M3 1h3l1.5 4-2 1.2a9 9 0 0 0 4.3 4.3L11 8.5l4 1.5v3a2 2 0 0 1-2 2A12 12 0 0 1 1 3a2 2 0 0 1 2-2z"/></svg>
          955 41 27 80
        </li>
        <li>
          <svg viewBox="0 0 16 16" aria-hidden="true"><path d="M1 3h14v10H1z M1 3l7 6 7-6" stroke="#1f1f21" stroke-width="1"/></svg>
          info@youremailaddress.com
        </li>
        <li>
          <svg viewBox="0 0 16 16" aria-hidden="true"><circle cx="8" cy="8" r="7"/></svg>
          www.yourdomainaddress.com
        </li>
      </ul>
    </div>
    <div class="bottom-band">
      <span class="band-red"></span>
      <span class="band-grey"></span>
    </div>
  </section>
</body>
</html>
```